Waterproofing Construction company needs letterhead

I need a letterhead design for a commercial waterproofing construction company. We would like to see designs that are contemporary, clean, sleek and use our logo. Our current design is dated. I would also like a cover page (see example) that goes with our letterhead. I would like for the footer to have our address, website, and phone number

Target Market(s)

Customers, potential customers.

Font styles to use
Sans Serif

Requirements
Must have
• logo, website, address, phone numbers, only our colors, tahoma font
• PMS: 295C PMS: 2995C
• CMYK: 100/84/36/39 CMYK: 80/12/1/0
• RGB: 16/44/82 RGB: 0/167/224
• HEX#: #102C52 HEX#: #00A7E0
• Black & White: 100% Black & White: 32%
• Gray Scale: 90% Gray Scale: 32%
Nice to have
• Our "icon" logo attached would be nice somewhere on the page.

```html
<!DOCTYPE html>
<html lang="en">
<head>
<meta charset="utf-8">
<title>Corvane Letterhead</title>
<link rel="stylesheet" href="https://fonts.googleapis.com/css2?family=Didact+Gothic&family=Open+Sans:wght@400&display=swap">
<style>
  :root {
    --navy: #102C52;
    --sky: #00A7E0;
    --ink: #5a5a5a;
    --ink-soft: #6b6b6b;
    --rule: #c9c9c9;
    --paper: #f5f5f5;
    --paper-edge: #ececec;
    --signature-tint: #d7e9f5;
  }
  * { margin: 0; padding: 0; box-sizing: border-box; }
  html, body { width: 861px; height: 1200px; overflow: hidden; }
  body {
    background: linear-gradient(90deg, var(--paper) 0%, #fafafa 45%, var(--paper-edge) 100%);
    font-family: "Didact Gothic", "Century Gothic", sans-serif;
    color: var(--ink);
    position: relative;
  }
  .brand { position: absolute; left: 72px; top: 84px; }
  .brand-name {
    display: flex; align-items: center; gap: 10px;
    font-size: 52px; line-height: 1; letter-spacing: 1px; color: var(--navy);
  }
  .brand-square { width: 22px; height: 22px; background: var(--sky); }
  .brand-tagline {
    margin-top: 6px; font-size: 12.5px; letter-spacing: 0.3px;
    color: var(--navy); text-transform: uppercase;
  }
  .contact {
    position: absolute; top: 97px; left: 0; width: 861px;
    font-family: "Open Sans", sans-serif; font-size: 12.5px; color: var(--ink-soft);
  }
  .contact-address {
    position: absolute; right: 221px; top: 9px; text-align: right; line-height: 16px;
  }
  .contact-divider {
    position: absolute; left: 654px; top: 0; width: 1px; height: 56px; background: var(--rule);
  }
  .contact-lines { position: absolute; left: 672px; top: 2px; list-style: none; }
  .contact-lines li { display: flex; align-items: center; gap: 6px; height: 17px; }
  .contact-lines svg { width: 11px; height: 11px; fill: var(--navy); }
  .letter { position: absolute; left: 77px; top: 272px; width: 713px; }
  .salutation { font-size: 22px; color: var(--ink); margin-bottom: 72px; }
  .letter p {
    font-size: 11.2px; line-height: 15px; text-align: justify; margin-bottom: 18px;
    hyphens: auto;
  }
  .closing { font-size: 11.2px; position: absolute; left: 77px; top: 765px; }
  .signature {
    position: absolute; left: 70px; top: 812px; width: 150px; height: 60px;
    background: linear-gradient(90deg, var(--signature-tint), rgba(215,233,245,0.3));
    border-radius: 6px;
  }
  .service-area {
    position: absolute; left: 0; width: 861px; top: 1131px;
    text-align: center; font-family: "Open Sans", sans-serif; font-size: 12.5px; color: var(--ink-soft);
  }
</style>
</head>
<body>
  <header>
    <div class="brand">
      <div class="brand-name"><span>CORVANE</span><span class="brand-square"></span></div>
      <div class="brand-tagline">Waterproofing • Restoration</div>
    </div>
    <div class="contact">
      <address class="contact-address">PO Box 417, Lindale,<br>NC 27390</address>
      <div class="contact-divider"></div>
      <ul class="contact-lines">
        <li><svg viewBox="0 0 12 12"><path d="M1 4c0-2 2-3 5-3s5 1 5 3v1H8V4H4v1H1zM3 6h6l2 5H1z"/></svg>(877) 555-0162</li>
        <li><svg viewBox="0 0 12 12"><path d="M3 1h6v3H3zM1 5h10v4H9v2H3V9H1zM4 8v2h4V8z"/></svg>(919) 555-0147</li>
        <li><svg viewBox="0 0 12 12"><circle cx="6" cy="6" r="5.5"/><path d="M1 6h10M6 .5v11" stroke="#f5f5f5" stroke-width="1" fill="none"/></svg>www.corvanewp.com</li>
      </ul>
    </div>
  </header>

  <main class="letter">
    <h1 class="salutation" style="font-weight:400">Dear Mr. Hale,</h1>
    <p>Lorem ipsum dolor sit amet, consectetur adipiscing elit. Donec orci purus, luctus vitae dignissim eu, iaculis sed purus. Vivamus faucibus, ipsum nec aliquet viverra, leo mauris condimentum ligula, sit amet sagittis enim ligula quis arcu. Nam egestas tortor id nisi porttitor mattis. In tortor ante, ultricies in suscipit a, tempus non massa. Vivamus et auctor mi. Fusce vel massa nulla. Phasellus nec eros mauris, et scelerisque orci.</p>
    <p>Donec malesuada orci vitae nulla accumsan porta a id massa. Quisque accumsan iaculis magna sit amet fringilla. Maecenas consequat, magna eget tincidunt semper, odio nibh rutrum mi, id feugiat ante nisi eu risus. Vestibulum nunc orci, rhoncus a placerat in, ultricies in mi. Cras mattis varius eros, vel fringilla nisi suscipit eget. Quisque scelerisque sagittis nulla at porttitor.</p>
    <p>Sed id augue vitae urna euismod commodo aliquet a quam. Pellentesque arcu velit, cursus et malesuada ut, consequat et diam. Nullam erat sem, rhoncus id ullamcorper vitae, rhoncus et arcu. In ultricies ultricies nulla, ut rutrum nisi iaculis at. Donec eu magna a metus ornare faucibus. Fusce aliquet faucibus ultricies. Morbi semper, est id tincidunt gravida, sem arcu adipiscing lacus, ac bibendum nulla leo eu purus. Quisque nec diam sed risus consectetur a ccumsan quis quis nibh. Vestibulum id purus lorem.</p>
    <p>It is a long established fact that a reader will be distracted by the readable content of a page when looking at its layout. The point of using Lorem Ipsum is that it has a more-or-less normal distribution of letters, as opposed to using 'Content here, content here', making it look like readable English. Many desktop publishing packages</p>
  </main>

  <div class="closing">Sincerely,</div>
  <div class="signature" role="img" aria-label="Handwritten signature of Owen Hale"></div>

  <footer class="service-area">North Carolina | South Carolina | Virginia</footer>
</body>
</html>
```